Square Business Cards for Our Restaurant / Event Venue

We need square business cards designed for the management team of our event venue and restaurant. On one side of the card should be the the Harbor Lantern 7 logo and URL www.harborlantern7.example. On the other side should be the Ember Logo and URL www.emberhall7.example. All employee details should be on the side with Ember logo. There will be a total of 5 cards to be created with the design.

Clara Bennquist
clara@harborlantern7.example

main 555.418.3072
direct 555.730.2946

4831 West Orchard Lane SE
Washington, DC 90417

Industry/Entity Type

Business

```html
<!DOCTYPE html>
<html lang="en">
<head>
<meta charset="utf-8">
<title>Harbor Lantern 7 – Square Business Cards</title>
<link rel="stylesheet" href="https://fonts.googleapis.com/css2?family=Open+Sans:wght@400;600;700&display=swap">
<style>
  :root {
    --backdrop: #808080;
    --card-dark: #000000;
    --card-light: #ffffff;
    --ink-light: #ffffff;
    --accent-red: #b81f25;
    --rule-grey: #c8c8c8;
    --card-shadow: rgba(0, 0, 0, 0.55);
  }
  * { box-sizing: border-box; margin: 0; padding: 0; }
  html, body {
    width: 1200px;
    height: 900px;
    overflow: hidden;
    background: var(--backdrop);
    font-family: "Open Sans", Arial, sans-serif;
  }
  .card {
    position: absolute;
    top: 259px;
    width: 393px;
    height: 393px;
    box-shadow: 3px 3px 4px var(--card-shadow);
    text-align: center;
  }
  .card--contact { left: 197px; background: var(--card-dark); color: var(--ink-light); }
  .card--brand { left: 614px; background: var(--card-light); }

  .ember-mark {
    position: absolute;
    top: 38px;
    left: 0;
    width: 100%;
    display: flex;
    justify-content: center;
    align-items: center;
    gap: 10px;
  }
  .ember-mark__dot {
    width: 14px; height: 14px;
    border-radius: 50%;
    background: var(--accent-red);
  }
  .ember-mark__name {
    font-size: 58px;
    font-weight: 700;
    line-height: 1;
    color: var(--ink-light);
  }
  .ember-url {
    position: absolute;
    top: 124px;
    right: 44px;
    font-size: 13px;
    color: var(--accent-red);
  }
  .person {
    position: absolute;
    top: 172px;
    left: 0;
    width: 100%;
  }
  .person__name { font-size: 18px; font-weight: 700; line-height: 24px; }
  .person__surname { color: var(--accent-red); }
  .person__email { font-size: 16px; line-height: 24px; }

  .phones {
    position: absolute;
    top: 248px;
    left: 0;
    width: 100%;
    list-style: none;
    font-size: 16px;
    line-height: 23px;
  }
  .phones__icon { width: 14px; height: 11px; margin-right: 6px; vertical-align: -1px; fill: var(--accent-red); }

  .address {
    position: absolute;
    top: 315px;
    left: 0;
    width: 100%;
    font-style: normal;
    font-size: 16px;
    line-height: 23px;
  }

  .harbor-mark {
    position: absolute;
    top: 118px;
    left: 0;
    width: 100%;
    display: flex;
    flex-direction: column;
    align-items: center;
    gap: 14px;
  }
  .harbor-mark__dot {
    width: 34px; height: 34px;
    border-radius: 50%;
    background: var(--accent-red);
  }
  .harbor-mark__name {
    font-size: 30px;
    font-weight: 400;
    color: var(--accent-red);
  }
  .harbor-url {
    position: absolute;
    top: 284px;
    left: 0;
    width: 100%;
    display: flex;
    align-items: center;
    gap: 8px;
    font-size: 16px;
    color: var(--accent-red);
  }
  .harbor-url::before, .harbor-url::after {
    content: "";
    flex: 1;
    height: 1px;
    background: var(--rule-grey);
  }
</style>
</head>
<body>
  <section class="card card--contact" aria-label="Contact side">
    <div class="ember-mark">
      <span class="ember-mark__name">Ember</span>
      <span class="ember-mark__dot"></span>
    </div>
    <p class="ember-url">www.emberhall7.example</p>

    <div class="person">
      <p class="person__name">Clara <span class="person__surname">Bennquist</span></p>
      <p class="person__email">clara@harborlantern7.example</p>
    </div>

    <ul class="phones">
      <li><svg class="phones__icon" viewBox="0 0 14 11" aria-hidden="true"><path d="M1 3.5C1 1.5 3.5 1 7 1s6 .5 6 2.5v1H10V3.2H4V4.5H1z"/><path d="M3.5 5.5h7l2 4.5H1.5z"/></svg>555.418.3072 (Main)</li>
      <li><svg class="phones__icon" viewBox="0 0 14 11" aria-hidden="true"><path d="M1 3.5C1 1.5 3.5 1 7 1s6 .5 6 2.5v1H10V3.2H4V4.5H1z"/><path d="M3.5 5.5h7l2 4.5H1.5z"/></svg>555.730.2946 (Direct)</li>
    </ul>

    <address class="address">
      4831 West Orchard Lane<br>
      SE Washington, DC 90417
    </address>
  </section>

  <section class="card card--brand" aria-label="Brand side">
    <div class="harbor-mark">
      <span class="harbor-mark__dot"></span>
      <span class="harbor-mark__name">Harbor Lantern 7</span>
    </div>
    <p class="harbor-url">www.harborlantern7.example</p>
  </section>
</body>
</html>
```